Urgent - brand new business card for a startup technical advisory and incubation business in Sydney

We need a brand new business card design for BrightForge. We are a startup technical advisory and incubation business based in Sydney Australia. We work with entrepreneurs and innovators to help rapidly and efficiently turn their ideas into reality and to ensure they have the technical platform required for growth.

Our name is partly inspired by our love of lean product development methods and the lean startup movement.

We would like clean, uncluttered designs that feature our two logo colours and communicate a professional but creative, in-touch and entrepreneurial business.

PLEASE SEE MUST HAVE PRIORITIES FOR DRAFT CONTACT INFORMATION AND OTHER DESIRED TEXT ON CARD.
Updates

We have now updated the brief to include draft business card contact information and also some additional desired text to feature on the card design.    Please review the Must Have priorities.

Also final updated source files for the horizontal and vertical versions have now been uploaded and should be used for any designs.

Thanks!

Target Market(s)

Entrepeneurs, innovators, startup investors looking for a strong product development partner

Industry/Entity Type

Business

Requirements
Must have
• Feature our two logo colours
Be a relatively clean, pared back overall design - quite minimalist

Updated source files (AI) for vertical and horizontal layouts attached.

Draft contact information for business card:
Neil Barton
Founder & CTO
Phone: +61 427 555123
Email: xxxx@brightforge.com
Skype: xxxxxbarton
Twitter: nbarton

www.brightforge.com

We would also like the overall design to include the phrase "You have great ideas. Let us make them happen." (probably in a reasonably subtle way)

Nice to have
• Inspire me! Double-sided designs are fine with logo, phrase, (URL?) on one side and contact details on other (+ any other design elements)

Logo on business card can be either with lightbulb above the wording as per example here or to the left of the BrightForge wording - both layouts in files provided.
Should not have
• Shouldn't look like a Pentara Suite business card template :-)

```html
<!DOCTYPE html>
<html lang="en">
<head>
<meta charset="UTF-8">
<title>BrightForge Business Card</title>
<link href="https://fonts.googleapis.com/css2?family=Source+Sans+3:wght@400;600;700&display=swap" rel="stylesheet">
<style>
  :root {
    --backdrop: #e4e5e7;
    --card: #ffffff;
    --brand-blue: #27a9e1;
    --ink: #1b1b1d;
    --muted: #6b6d70;
    --dark-top: #1a1a1c;
    --dark-mid: #55575b;
    --dark-light: #a5a7aa;
    --wave-deep: #4f7186;
    --wave-mid: #8fb4c8;
    --wave-light: #e8f1f6;
  }
  * { box-sizing: border-box; margin: 0; padding: 0; }
  html, body {
    width: 1200px;
    height: 1200px;
    overflow: hidden;
    background: var(--backdrop);
    font-family: "Source Sans 3", "Myriad Pro", sans-serif;
  }
  .sheet {
    position: relative;
    width: 1200px;
    height: 1200px;
  }
  .card {
    position: absolute;
    left: 160px;
    width: 880px;
    height: 503px;
    background: var(--card);
    overflow: hidden;
    box-shadow: 0 6px 20px rgba(0,0,0,0.12);
  }
  .card--front { top: 76px; }
  .card--back { top: 621px; }
  .card__art {
    position: absolute;
    inset: 0;
    width: 100%;
    height: 100%;
  }
  .brand {
    position: absolute;
    left: 58px;
    top: 70px;
    display: flex;
    align-items: center;
    gap: 14px;
  }
  .brand__dot {
    width: 34px;
    height: 34px;
    border-radius: 50%;
    background: var(--brand-blue);
  }
  .brand__name {
    font-size: 54px;
    font-weight: 700;
    color: var(--brand-blue);
    letter-spacing: -0.5px;
  }
  .contact {
    position: absolute;
    right: 58px;
    top: 262px;
    text-align: right;
    color: var(--ink);
  }
  .contact__name {
    font-size: 30px;
    font-weight: 700;
    letter-spacing: -0.3px;
    line-height: 1;
    text-transform: uppercase;
  }
  .contact__role {
    font-size: 16px;
    color: var(--muted);
    margin-bottom: 14px;
  }
  .contact__line {
    font-size: 22px;
    line-height: 27px;
  }
  .contact__label { color: var(--brand-blue); }
</style>
</head>
<body>
<main class="sheet">

  <section class="card card--front" aria-label="Business card front">
    <svg class="card__art" viewBox="0 0 880 503" preserveAspectRatio="none">
      <defs>
        <linearGradient id="frontDark" x1="0" y1="0" x2="1" y2="1">
          <stop offset="0" stop-color="var(--dark-top)"/>
          <stop offset="0.6" stop-color="var(--dark-mid)"/>
          <stop offset="1" stop-color="var(--dark-light)"/>
        </linearGradient>
        <linearGradient id="frontWave" x1="0" y1="0" x2="0" y2="1">
          <stop offset="0" stop-color="var(--wave-light)"/>
          <stop offset="0.35" stop-color="var(--wave-mid)"/>
          <stop offset="0.6" stop-color="var(--wave-deep)"/>
          <stop offset="0.85" stop-color="var(--wave-mid)"/>
          <stop offset="1" stop-color="var(--wave-light)"/>
        </linearGradient>
      </defs>
      <path class="dark-field" d="M0,335 C250,350 500,420 880,375 L880,503 L0,503 Z" fill="url(#frontDark)"/>
      <path role="img" aria-label="Flowing blue and white stripe wave" d="M0,225 C200,240 400,300 880,255 L880,375 C500,420 250,350 0,335 Z" fill="url(#frontWave)"/>
    </svg>
    <div class="brand">
      <span class="brand__dot"></span>
      <span class="brand__name">BrightForge</span>
    </div>
  </section>

  <section class="card card--back" aria-label="Business card back">
    <svg class="card__art" viewBox="0 0 880 503" preserveAspectRatio="none">
      <defs>
        <linearGradient id="backDark" x1="0" y1="0" x2="1" y2="1">
          <stop offset="0" stop-color="var(--dark-light)"/>
          <stop offset="0.5" stop-color="var(--dark-mid)"/>
          <stop offset="1" stop-color="var(--dark-top)"/>
        </linearGradient>
        <linearGradient id="backWave" x1="0" y1="0" x2="0" y2="1">
          <stop offset="0" stop-color="var(--wave-light)"/>
          <stop offset="0.35" stop-color="var(--wave-mid)"/>
          <stop offset="0.6" stop-color="var(--wave-deep)"/>
          <stop offset="0.85" stop-color="var(--wave-mid)"/>
          <stop offset="1" stop-color="var(--wave-light)"/>
        </linearGradient>
      </defs>
      <path class="dark-field" d="M0,0 L880,0 L880,80 C450,110 250,290 0,300 Z" fill="url(#backDark)"/>
      <path role="img" aria-label="Flowing blue and white stripe wave" d="M0,300 C250,290 450,110 880,80 L880,215 C500,230 300,420 0,440 Z" fill="url(#backWave)"/>
    </svg>
    <div class="contact">
      <p class="contact__name">Neil Barton</p>
      <p class="contact__role">Founder &amp; CTO</p>
      <p class="contact__line"><span class="contact__label">Phone:</span> +61 427 555123</p>
      <p class="contact__line"><span class="contact__label">Email:</span> xxxx@brightforge.com</p>
      <p class="contact__line"><span class="contact__label">Website:</span> www.brightforge.com</p>
      <p class="contact__line"><span class="contact__label">Skype:</span> xxxxxbarton</p>
      <p class="contact__line"><span class="contact__label">Twitter:</span> nbarton</p>
    </div>
  </section>

</main>
</body>
</html>
```